Product Sales Website Design - E-commerce - Shopify etc

We have been selling printing equipment for some time now and think that it will be useful to sell the products on the internet, using a simple e-commerce platform, such as shopify etc. There are roughly a few dozen products - so basically, the idea is to have a modern, simple and clean home page. When someone looks at it, they think, this is it - I want to buy here. I am not going to impose any ideas or say how I want it done.

Just so you know, at the moment there are three categories of products. One being printers, scanners and accessories.

I am excited by this whole project and don't want to have good designers backing out because they feel i am imposing restrictions. Feel free to impress me.

Industry/Entity Type

E-Commerce

Requirements
Must have
• integration with an e-commerce platform is a must or show how to integrate, so I can easily introduce further products.

```html
<!DOCTYPE html>
<html lang="en">
<head>
<meta charset="utf-8">
<title>Printhaven Store – Home</title>
<link href="https://fonts.googleapis.com/css2?family=Open+Sans:wght@400;600;700&display=swap" rel="stylesheet">
<style>
:root{
  --page:#e4e4e4;
  --white:#ffffff;
  --navy:#1f4e8c;
  --sky:#6aa4e8;
  --crimson:#c41e4f;
  --green:#6cbf3f;
  --tag:#8e99aa;
  --price-bar:#8e99aa;
  --cart:#5aa3e8;
  --wish:#f8a83a;
  --text:#444b55;
  --muted:#7a7f87;
  --footer:#1e2935;
  --footer-text:#e8ecf0;
  --tile-blue:#3b5998;
  --tile-amber:#f7b52b;
  --tile-red:#e4335a;
  --tile-cyan:#42ade2;
}
*{box-sizing:border-box;margin:0;padding:0}
html,body{width:1026px;height:1200px;overflow:hidden;background:var(--page);font-family:"Open Sans",sans-serif;color:var(--text)}
.canvas{position:relative;width:1026px;height:1200px}
.abs{position:absolute}

/* sidebar */
.deal{left:69px;top:26px;width:204px;height:134px;background:var(--navy);color:var(--white);padding:14px 10px}
.deal h3{font-size:13px;font-weight:700;display:flex;align-items:center;gap:12px;margin-left:0}
.deal p{font-size:9px;line-height:14px;margin:10px 0 8px}
.deal form{display:flex;height:30px}
.deal input{flex:1;border:0;font:9px "Open Sans",sans-serif;padding:0 6px;color:var(--muted)}
.deal button{width:36px;border:0;background:var(--green);display:flex;align-items:center;justify-content:center}

.panel{background:var(--white)}
.panel-head{height:46px;background:var(--green);color:var(--white);display:flex;align-items:center;gap:14px;padding-left:8px;font-size:14px;font-weight:600}
.badge-icon{width:30px;height:30px;border-radius:50%;border:2px solid var(--white);display:flex;align-items:center;justify-content:center}
.tags{left:69px;top:186px;width:204px;height:192px}
.tag-list{display:flex;flex-wrap:wrap;gap:6px 7px;padding:15px 9px}
.tag{background:var(--tag);color:var(--white);font-size:10px;border-radius:9px;padding:2px 10px 2px 13px;position:relative}
.tag::before{content:"";position:absolute;left:5px;top:8px;width:4px;height:4px;border-radius:50%;background:var(--white)}
.special{left:69px;top:401px;width:204px;height:292px}
.special-img{margin:20px auto 0;width:140px;height:98px;background:linear-gradient(160deg,#3a3d42,#15171a 60%,#8a4cc2);border-radius:3px}
.special p{font-size:10px;line-height:16px;text-align:justify;padding:0 9px;margin-top:26px;color:var(--text)}
.readmore{display:block;text-align:right;font-size:9px;color:var(--green);padding-right:9px;margin-top:4px}
.slider{position:absolute;left:0;bottom:0;width:204px;height:14px;background:#e9edf2}
.slider span{display:block;width:26px;height:14px;background:#b9cff0;margin-left:16px}

.tile{width:98px;height:98px;display:flex;align-items:center;justify-content:center;color:var(--white);font-size:13px;font-weight:700}
.t-friend{left:69px;top:717px;background:var(--tile-blue)}
.t-feed{left:176px;top:717px;background:var(--tile-amber)}
.t-clip{left:69px;top:823px;background:var(--tile-red)}
.t-chirp{left:176px;top:823px;background:var(--tile-cyan)}

/* tabs */
.tab{top:17px;height:68px;color:var(--white);font-size:11px;display:flex;flex-direction:column;align-items:center;justify-content:flex-end;padding-bottom:12px;gap:8px}
.tab-latest{left:296px;width:112px;background:var(--navy)}
.tab-latest::after{content:"";position:absolute;bottom:-9px;left:50%;margin-left:-9px;border:9px solid transparent;border-bottom:0;border-top-color:var(--navy)}
.tab-popular{left:413px;width:118px;background:var(--sky)}
.tab-best{left:536px;width:86px;background:var(--sky)}
.shipping{left:626px;top:17px;width:331px;height:68px;background:var(--crimson);color:var(--white);display:flex;align-items:center;gap:18px;padding-left:18px}
.shipping strong{display:block;font-size:18px;font-weight:700;line-height:22px}
.shipping span{font-size:13px}

/* products */
.card{width:209px;height:245px;background:var(--white)}
.card .photo{position:absolute;left:14px;top:14px;width:181px;height:140px;background:linear-gradient(165deg,#f5f5f5 0%,#3b3e44 35%,#141518 65%,#9d55c9 85%,#f5f5f5 100%);border-radius:3px}
.card .name{position:absolute;top:170px;width:100%;text-align:center;font-size:12.5px;color:var(--text)}
.price-bar{position:absolute;left:0;bottom:0;width:100%;height:38px;background:var(--price-bar);display:flex;align-items:center;color:var(--white)}
.price{font-size:14px;font-weight:700;padding-left:9px;flex:1}
.price s{font-weight:400;font-size:12px;margin-left:10px;opacity:.9}
.btn{width:36px;height:38px;display:flex;align-items:center;justify-content:center}
.btn-cart{background:var(--cart)}
.btn-wish{background:var(--wish)}

/* footer */
.footer{left:69px;top:945px;width:888px;height:195px;background:var(--footer);color:var(--footer-text);padding:17px 11px;display:flex}
.footer h4{font-size:15px;font-weight:400;margin-bottom:10px}
.footer ul{list-style:none;font-size:10.5px;line-height:18px}
.col-info{width:152px}
.col-why{width:152px}
.col-contact{width:308px;font-size:10.5px;line-height:17px}
.col-contact b{font-weight:700}
.gap{height:17px}
.feed{flex:1;padding-left:2px}
.post{display:flex;gap:8px;margin-bottom:20px}
.avatar{width:36px;height:36px;background:var(--white);flex:none}
.post-body{flex:1;font-size:10.5px;line-height:13px}
.post-head{display:flex;justify-content:space-between;font-weight:700}
.post-head span{font-weight:400;color:#9aa3ad;font-size:9.5px}
.hash{color:var(--green)}

.copyright{left:69px;top:1158px;font-size:10.5px;color:var(--text)}
.copyright em{font-style:normal;color:var(--green);margin-left:6px;font-size:12px}
.cards{left:726px;top:1148px;display:flex;gap:8px}
.pay{width:50px;height:34px;background:var(--white);border-radius:3px;display:flex;align-items:center;justify-content:center;font-size:9.5px;font-weight:700;color:var(--text);box-shadow:0 1px 2px rgba(0,0,0,.25)}
.to-top{left:981px;top:1145px;width:34px;height:34px;background:var(--wish);border-radius:3px;display:flex;align-items:center;justify-content:center}
</style>
</head>
<body>
<div class="canvas">

  <aside>
    <section class="deal abs">
      <h3><svg width="16" height="12" viewBox="0 0 16 12"><rect x="0.5" y="0.5" width="15" height="11" fill="none" stroke="#fff"/><path d="M1 1l7 6 7-6" fill="none" stroke="#fff"/></svg>GET DEAL</h3>
      <p>Get exclusive deal offers delivered right to your inbox</p>
      <form><input type="text" placeholder="Enter your email..."><button type="button" aria-label="Subscribe"><svg width="22" height="22" viewBox="0 0 22 22"><circle cx="11" cy="11" r="9.5" fill="none" stroke="#fff" stroke-width="1.5"/><path d="M6 11h9M11 7l4 4-4 4" fill="none" stroke="#fff" stroke-width="1.8"/></svg></button></form>
    </section>

    <section class="tags abs panel">
      <div class="panel-head"><span class="badge-icon"><svg width="14" height="14" viewBox="0 0 24 24"><path d="M12 2l3 7 7 .6-5.3 4.7 1.6 7.2L12 17.8 5.7 21.5l1.6-7.2L2 9.6 9 9z" fill="#fff"/></svg></span>POPULAR TAGS</div>
      <div class="tag-list">
        <span class="tag">Aenean</span><span class="tag">fusce</span><span class="tag">Morbi</span>
        <span class="tag">ante</span><span class="tag">condimentum</span>
        <span class="tag">consectetur</span><span class="tag">dolor</span><span class="tag">eget</span>
        <span class="tag">elementum</span><span class="tag">tincidunt</span>
        <span class="tag">volutpat</span>
      </div>
    </section>

    <section class="special abs panel">
      <div class="panel-head"><span class="badge-icon"><svg width="14" height="14" viewBox="0 0 24 24"><path d="M12 2l3 7 7 .6-5.3 4.7 1.6 7.2L12 17.8 5.7 21.5l1.6-7.2L2 9.6 9 9z" fill="#fff"/></svg></span>SPECIAL PRODUCT</div>
      <div class="special-img" role="img" aria-label="Photo of a black all-in-one printer with a colour print in the tray"></div>
      <p>Lorem ipsum dolor sit amet, consectetur adipiscing elit. In gravida pellentesque ligula, vel ...</p>
      <span class="readmore">Read more ▪</span>
      <div class="slider"><span></span></div>
    </section>

    <a class="tile abs t-friend">Friendsly</a>
    <a class="tile abs t-feed">Feedline</a>
    <a class="tile abs t-clip">Clipstream</a>
    <a class="tile abs t-chirp">Chirper</a>
  </aside>

  <nav>
    <div class="tab abs tab-latest"><svg width="22" height="24" viewBox="0 0 22 24"><circle cx="11" cy="14" r="8.5" fill="none" stroke="#fff" stroke-width="1.6"/><path d="M11 14V9M8 2h6M11 2v3" stroke="#fff" stroke-width="1.6" fill="none"/></svg>Latest Products</div>
    <div class="tab abs tab-popular"><svg width="22" height="24" viewBox="0 0 22 24"><rect x="3" y="8" width="16" height="14" fill="none" stroke="#fff" stroke-width="1.6"/><path d="M7 8V5a4 4 0 0 1 8 0v3" fill="none" stroke="#fff" stroke-width="1.6"/></svg>Popular Products</div>
    <div class="tab abs tab-best"><svg width="20" height="24" viewBox="0 0 20 24"><path d="M6 1l4 8 4-8" fill="none" stroke="#fff" stroke-width="1.6"/><circle cx="10" cy="16" r="6.5" fill="none" stroke="#fff" stroke-width="1.6"/></svg>Best Sales</div>
    <div class="shipping abs"><svg width="34" height="34" viewBox="0 0 34 34"><rect x="3" y="12" width="28" height="7" fill="none" stroke="#fff" stroke-width="2"/><rect x="5" y="19" width="24" height="13" fill="none" stroke="#fff" stroke-width="2"/><path d="M17 12v20M17 12c-3-8-11-8-9-3 1 2 6 3 9 3 3 0 8-1 9-3 2-5-6-5-9 3" fill="none" stroke="#fff" stroke-width="2"/></svg><div><strong>FREE SHIPPING</strong><span>On Orders Over $ 999</span></div></div>
  </nav>

  <main>
    <article class="card abs" style="left:296px;top:100px"><div class="photo" role="img" aria-label="Product photo of a black flatbed printer"></div><div class="name">Nate mila rita</div><div class="price-bar"><span class="price">$54.00</span><span class="btn btn-cart"><svg width="22" height="18" viewBox="0 0 22 18"><path d="M1 1h3l3 11h11l2-8H6" fill="none" stroke="#fff" stroke-width="1.6"/><circle cx="9" cy="16" r="1.5" fill="#fff"/><circle cx="16" cy="16" r="1.5" fill="#fff"/></svg></span><span class="btn btn-wish"><svg width="22" height="22" viewBox="0 0 22 22"><circle cx="11" cy="11" r="9.5" fill="none" stroke="#fff" stroke-width="1.6"/><path d="M11 16l-4.5-4.5a2.5 2.5 0 0 1 4.5-3 2.5 2.5 0 0 1 4.5 3z" fill="#fff"/></svg></span></div></article>
    <article class="card abs" style="left:522px;top:100px"><div class="photo" role="img" aria-label="Product photo of a black all-in-one printer"></div><div class="name">Hute bakom liza</div><div class="price-bar"><span class="price">$66.00<s>$76.00</s></span><span class="btn btn-cart"><svg width="22" height="18" viewBox="0 0 22 18"><path d="M1 1h3l3 11h11l2-8H6" fill="none" stroke="#fff" stroke-width="1.6"/><circle cx="9" cy="16" r="1.5" fill="#fff"/><circle cx="16" cy="16" r="1.5" fill="#fff"/></svg></span><span class="btn btn-wish"><svg width="22" height="22" viewBox="0 0 22 22"><circle cx="11" cy="11" r="9.5" fill="none" stroke="#fff" stroke-width="1.6"/><path d="M11 16l-4.5-4.5a2.5 2.5 0 0 1 4.5-3 2.5 2.5 0 0 1 4.5 3z" fill="#fff"/></svg></span></div></article>
    <article class="card abs" style="left:748px;top:100px"><div class="photo" role="img" aria-label="Product photo of a black flatbed printer"></div><div class="name">Kutan mula bako</div><div class="price-bar"><span class="price">$75.00</span><span class="btn btn-cart"><svg width="22" height="18" viewBox="0 0 22 18"><path d="M1 1h3l3 11h11l2-8H6" fill="none" stroke="#fff" stroke-width="1.6"/><circle cx="9" cy="16" r="1.5" fill="#fff"/><circle cx="16" cy="16" r="1.5" fill="#fff"/></svg></span><span class="btn btn-wish"><svg width="22" height="22" viewBox="0 0 22 22"><circle cx="11" cy="11" r="9.5" fill="none" stroke="#fff" stroke-width="1.6"/><path d="M11 16l-4.5-4.5a2.5 2.5 0 0 1 4.5-3 2.5 2.5 0 0 1 4.5 3z" fill="#fff"/></svg></span></div></article>
    <article class="card abs" style="left:296px;top:374px"><div class="photo" role="img" aria-label="Product photo of a black flatbed printer"></div><div class="name">Polan maze riga</div><div class="price-bar"><span class="price">$65.00</span><span class="btn btn-cart"><svg width="22" height="18" viewBox="0 0 22 18"><path d="M1 1h3l3 11h11l2-8H6" fill="none" stroke="#fff" stroke-width="1.6"/><circle cx="9" cy="16" r="1.5" fill="#fff"/><circle cx="16" cy="16" r="1.5" fill="#fff"/></svg></span><span class="btn btn-wish"><svg width="22" height="22" viewBox="0 0 22 22"><circle cx="11" cy="11" r="9.5" fill="none" stroke="#fff" stroke-width="1.6"/><path d="M11 16l-4.5-4.5a2.5 2.5 0 0 1 4.5-3 2.5 2.5 0 0 1 4.5 3z" fill="#fff"/></svg></span></div></article>
    <article class="card abs" style="left:522px;top:374px"><div class="photo" role="img" aria-label="Product photo of a black all-in-one printer"></div><div class="name"></div><div class="price-bar"><span class="price">$35.00</span><span class="btn btn-cart"><svg width="22" height="18" viewBox="0 0 22 18"><path d="M1 1h3l3 11h11l2-8H6" fill="none" stroke="#fff" stroke-width="1.6"/><circle cx="9" cy="16" r="1.5" fill="#fff"/><circle cx="16" cy="16" r="1.5" fill="#fff"/></svg></span><span class="btn btn-wish"><svg width="22" height="22" viewBox="0 0 22 22"><circle cx="11" cy="11" r="9.5" fill="none" stroke="#fff" stroke-width="1.6"/><path d="M11 16l-4.5-4.5a2.5 2.5 0 0 1 4.5-3 2.5 2.5 0 0 1 4.5 3z" fill="#fff"/></svg></span></div></article>
    <article class="card abs" style="left:748px;top:374px"><div class="photo" role="img" aria-label="Product photo of a black flatbed printer"></div><div class="name" style="top:155px">Kula vace tenca</div><div class="price-bar"><span class="price">$32.00</span><span class="btn btn-cart"><svg width="22" height="18" viewBox="0 0 22 18"><path d="M1 1h3l3 11h11l2-8H6" fill="none" stroke="#fff" stroke-width="1.6"/><circle cx="9" cy="16" r="1.5" fill="#fff"/><circle cx="16" cy="16" r="1.5" fill="#fff"/></svg></span><span class="btn btn-wish"><svg width="22" height="22" viewBox="0 0 22 22"><circle cx="11" cy="11" r="9.5" fill="none" stroke="#fff" stroke-width="1.6"/><path d="M11 16l-4.5-4.5a2.5 2.5 0 0 1 4.5-3 2.5 2.5 0 0 1 4.5 3z" fill="#fff"/></svg></span></div></article>
  </main>

  <footer class="footer abs">
    <div class="col-info"><h4>Information</h4><ul><li>Contact</li><li>Sitemap</li><li>Legal Notice</li><li>Terms and Conditions</li><li>About Us</li></ul></div>
    <div class="col-why"><h4>Why Choose Us</h4><ul><li>Shipping &amp; Returns</li><li>Secure Shopping</li><li>International Shipping</li><li>Affiliates</li><li>Group Sales</li></ul></div>
    <div class="col-contact"><h4>Contact us</h4>
      <div><b>Add 1 :</b> 40 Harbor Lane, Westbrook, Ohio, United States</div>
      <div><b>Add 2 :</b> 70 Mill Road, Westbrook, Ohio, United States</div>
      <div class="gap"></div>
      <div><b>Phone :</b> (555) - 01 - 04821937</div>
      <div style="padding-left:41px">(555) - 01 - 04821938</div>
      <div class="gap"></div>
      <div><b>Email :</b> contact@printhaven.example</div>
    </div>
    <div class="feed">
      <div class="post"><div class="avatar"></div><div class="post-body"><div class="post-head">Printhaven<span>4 Jan</span></div>There are some hours for getting 45% <span class="hash">#DISCOUNT</span> on <span class="hash">#SHOPWELL</span> products</div></div>
      <div class="post"><div class="avatar"></div><div class="post-body"><div class="post-head">Printhaven<span>12 Dec</span></div>Merry Christmas &amp; Happy New Year 2014 - Big Freebies from Inkwell Studio</div></div>
    </div>
  </footer>

  <div class="copyright abs">© 2013 Shopwell Demo Store. All Rights Reserved. Designed by <em>Northline Studio</em></div>
  <div class="cards abs"><span class="pay">Goldpay</span><span class="pay">Wingpay</span><span class="pay">Vexa</span><span class="pay">Meripay</span></div>
  <a class="to-top abs" aria-label="Back to top"><svg width="18" height="18" viewBox="0 0 18 18"><path d="M9 16V3M3 9l6-6 6 6" fill="none" stroke="#fff" stroke-width="2.4"/></svg></a>
</div>
</body>
</html>
```